E-Blast with US football theme

Hello, we are looking for an email blast with a US football theme (Grand Clash in the US is next weekend).
Specs:
600px w x 1500px h
Headline: Need Financing For A Win?
Winning teams donβt leave success to chanceβthey build a solid game plan.
Whether youβre expanding, constructing, refinancing, or making key acquisitions, QRV provides financing solutions that help you execute your strategy with confidence. Letβs work together to create a winning playbook.
Our custom financing solutions include:
π Acquisitions
π Construction
π Refinancing
π Recapitalizations
π Structured Leases
And our products include:
π Bridge
π Mezzanine
π Unitranche
π NNN Lease
π Preferred Equity

```html
<!DOCTYPE html>
<html lang="en">
<head>
<meta charset="utf-8">
<title>Need Financing For A Win? – QRV E-Blast</title>
<link rel="stylesheet" href="https://fonts.googleapis.com/css2?family=Oswald:wght@500;600;700&family=Montserrat:wght@400;500;700;800&display=swap">
<style>
  :root {
    --backdrop: #c0bec0;
    --navy: #0d2a8a;
    --navy-deep: #0a2a88;
    --ink: #13338f;
    --cta-blue: #0a74d0;
    --white: #ffffff;
    --sky-top: #142a8c;
    --sky-mid: #3d64cc;
    --sky-glow: #b9c6ee;
    --ball-brown: #7a3e22;
    --trophy-gold: #c99a1c;
    --accent-light: #6ec1f0;
  }
  * { margin: 0; padding: 0; box-sizing: border-box; }
  html, body {
    width: 1200px; height: 1200px; overflow: hidden;
    background: var(--backdrop);
  }
  .eblast {
    position: absolute; left: 388px; top: 70px;
    width: 424px; height: 1060px;
    background: var(--white);
    overflow: hidden;
  }
  .hero {
    position: absolute; left: 0; top: 0; width: 424px; height: 356px;
    background: linear-gradient(180deg, var(--sky-top) 0%, var(--sky-mid) 35%, #7f96de 62%, var(--sky-glow) 82%, var(--white) 100%);
  }
  .headline {
    position: absolute; left: 26px; top: 16px;
    font-family: 'Oswald', sans-serif; font-weight: 600;
    font-size: 66px; line-height: 70px; color: var(--white);
    letter-spacing: -0.5px;
  }
  .tagline {
    position: absolute; left: 20px; right: 20px; top: 354px;
    font-family: 'Oswald', sans-serif; font-weight: 700;
    font-size: 28px; line-height: 32px; color: var(--navy);
    text-align: center;
  }
  .intro {
    position: absolute; left: 20px; right: 20px; top: 530px;
    font-family: 'Montserrat', sans-serif; font-weight: 500;
    font-size: 13.6px; line-height: 21px; color: var(--ink);
    text-align: center;
  }
  .cta {
    position: absolute; left: 28px; top: 570px; width: 370px; height: 57px;
    background: var(--cta-blue); color: var(--white);
    font-family: 'Montserrat', sans-serif; font-weight: 800;
    font-size: 15.5px; line-height: 24px; text-align: center;
    padding-top: 4px;
  }
  .list-heading {
    position: absolute; left: 25px;
    font-family: 'Oswald', sans-serif; font-weight: 600;
    font-size: 22px; line-height: 26px; color: var(--navy);
  }
  .solutions-heading { top: 651px; }
  .products-heading { top: 829px; }
  .offer-list {
    position: absolute; left: 32px; list-style: none;
    font-family: 'Montserrat', sans-serif; font-weight: 700;
    font-size: 14.5px; line-height: 25px; color: var(--ink);
  }
  .solutions-list { top: 686px; }
  .products-list { top: 864px; }
  .offer-list li { display: flex; align-items: center; gap: 6px; }
  .offer-list svg { width: 13px; height: 13px; flex: none; }
  .footer {
    position: absolute; left: 0; bottom: 0; width: 424px; height: 59px;
    background: var(--navy-deep);
  }
  .footer-url {
    position: absolute; left: 25px; top: 20px;
    font-family: 'Montserrat', sans-serif; font-weight: 700;
    font-size: 14.5px; color: var(--white);
  }
  .brand {
    position: absolute; right: 28px; top: 12px;
    display: flex; align-items: center; gap: 8px;
  }
  .brand-mark { width: 16px; height: 16px; background: var(--accent-light); }
  .brand-name {
    font-family: 'Montserrat', sans-serif; font-weight: 700;
    font-size: 28px; line-height: 34px; color: var(--white);
  }
</style>
</head>
<body>
  <main class="eblast">
    <div class="hero" role="img" aria-label="Football player in a yellow jersey leaping to catch the ball under bright stadium lights"></div>
    <h1 class="headline">Need Financing<br>For A Win?</h1>

    <h2 class="tagline">Winning teams don’t leave success to chance—they build a solid game plan.</h2>

    <p class="intro" style="top:469px">Whether you’re expanding, constructing,<br>refinancing, or making key acquisitions,<br>QRV provides financing solutions that help you<br>execute your strategy with confidence.</p>

    <div class="cta">Let’s work together<br>to create a winning playbook.</div>

    <h3 class="list-heading solutions-heading">Our custom financing solutions include:</h3>
    <ul class="offer-list solutions-list">
      <li><svg viewBox="0 0 14 14" aria-hidden="true"><ellipse cx="7" cy="7" rx="6.5" ry="4" transform="rotate(-35 7 7)" fill="var(--ball-brown)"/><line x1="5" y1="8.5" x2="9" y2="5.5" stroke="#fff" stroke-width="1"/></svg>Acquisitions</li>
      <li><svg viewBox="0 0 14 14" aria-hidden="true"><ellipse cx="7" cy="7" rx="6.5" ry="4" transform="rotate(-35 7 7)" fill="var(--ball-brown)"/><line x1="5" y1="8.5" x2="9" y2="5.5" stroke="#fff" stroke-width="1"/></svg>Construction</li>
      <li><svg viewBox="0 0 14 14" aria-hidden="true"><ellipse cx="7" cy="7" rx="6.5" ry="4" transform="rotate(-35 7 7)" fill="var(--ball-brown)"/><line x1="5" y1="8.5" x2="9" y2="5.5" stroke="#fff" stroke-width="1"/></svg>Refinancing</li>
      <li><svg viewBox="0 0 14 14" aria-hidden="true"><ellipse cx="7" cy="7" rx="6.5" ry="4" transform="rotate(-35 7 7)" fill="var(--ball-brown)"/><line x1="5" y1="8.5" x2="9" y2="5.5" stroke="#fff" stroke-width="1"/></svg>Recapitalizations</li>
      <li><svg viewBox="0 0 14 14" aria-hidden="true"><ellipse cx="7" cy="7" rx="6.5" ry="4" transform="rotate(-35 7 7)" fill="var(--ball-brown)"/><line x1="5" y1="8.5" x2="9" y2="5.5" stroke="#fff" stroke-width="1"/></svg>Structured Leases</li>
    </ul>

    <h3 class="list-heading products-heading">And our products include:</h3>
    <ul class="offer-list products-list">
      <li><svg viewBox="0 0 14 14" aria-hidden="true"><path d="M3 1h8v4a4 4 0 0 1-8 0z M6 9h2v2h2v2H4v-2h2z" fill="var(--trophy-gold)"/></svg>Bridge</li>
      <li><svg viewBox="0 0 14 14" aria-hidden="true"><path d="M3 1h8v4a4 4 0 0 1-8 0z M6 9h2v2h2v2H4v-2h2z" fill="var(--trophy-gold)"/></svg>Mezzanine</li>
      <li><svg viewBox="0 0 14 14" aria-hidden="true"><path d="M3 1h8v4a4 4 0 0 1-8 0z M6 9h2v2h2v2H4v-2h2z" fill="var(--trophy-gold)"/></svg>Unitranche</li>
      <li><svg viewBox="0 0 14 14" aria-hidden="true"><path d="M3 1h8v4a4 4 0 0 1-8 0z M6 9h2v2h2v2H4v-2h2z" fill="var(--trophy-gold)"/></svg>NNN Lease</li>
      <li><svg viewBox="0 0 14 14" aria-hidden="true"><path d="M3 1h8v4a4 4 0 0 1-8 0z M6 9h2v2h2v2H4v-2h2z" fill="var(--trophy-gold)"/></svg>Preferred Equity</li>
    </ul>

    <footer class="footer">
      <span class="footer-url">www.qrvcapital.com</span>
      <div class="brand">
        <span class="brand-mark"></span>
        <span class="brand-name">QRV</span>
      </div>
    </footer>
  </main>
</body>
</html>
```